Full service residential and commercial painting
Finest quality attention to detail
All workmanship guaranteed
Email :norabvantreel@mailbox-example.fr
Mobile: 0417382650
Industry/Entity Type
Residential
Contact Information for Business Card
Henri marsot painting & decorating
Requirements
Nice to have
- Am thinking about someone can be painting my name on the card with HM painting with the logos of brush,pot tray and roller sleeves

```html
<!DOCTYPE html>
<html lang="en">
<head>
<meta charset="utf-8">
<title>Henri marsot painting &amp; decorating – business card</title>
<link rel="stylesheet" href="https://fonts.googleapis.com/css2?family=Josefin+Sans:wght@400&family=Pinyon+Script&display=swap">
<style>
  :root {
    --page: #ffffff;
    --card: #ffffff;
    --sage: #c7cfb6;
    --ink-blue: #2f6fb3;
    --ink-brown: #6e5548;
    --parchment-light: #e6c3ad;
    --parchment-mid: #dcb59c;
    --parchment-dark: #c99e83;
    --contact: #8a6f5f;
  }
  * { margin: 0; padding: 0; box-sizing: border-box; }
  html, body {
    width: 891px; height: 1200px; overflow: hidden;
    background: var(--page);
  }
  .business-card {
    position: absolute;
    left: 115px; top: 62px;
    width: 660px; height: 1075px;
    background: var(--card);
    overflow: hidden;
    box-shadow: 0 0 0 1px #eeeeee;
  }
  .card-art { position: absolute; inset: 0; }
  .business-name {
    position: absolute; top: 80px; left: 0; right: 0;
    text-align: center;
    font-family: "Josefin Sans", sans-serif;
    font-weight: 400;
    color: var(--ink-brown);
    font-size: 38px;
    line-height: 1.35;
  }
  .services {
    position: absolute; top: 340px; left: 60px; right: 40px;
    list-style: none;
    font-family: "Pinyon Script", cursive;
    color: var(--ink-blue);
    font-size: 37px;
    line-height: 80px;
    letter-spacing: 3px;
  }
  .contact {
    position: absolute; top: 885px; left: 70px;
    list-style: none;
    font-family: "Josefin Sans", sans-serif;
    font-weight: 400;
    color: var(--contact);
    font-size: 23px;
    line-height: 50px;
  }
  .contact li { display: flex; align-items: center; gap: 12px; }
  .contact .icon { width: 22px; height: 22px; flex: none; }
</style>
</head>
<body>
  <article class="business-card">
    <svg class="card-art" width="660" height="1075" viewBox="0 0 660 1075">
      <defs>
        <linearGradient id="parchment" x1="0" y1="0" x2="1" y2="1">
          <stop offset="0" stop-color="var(--parchment-mid)"/>
          <stop offset="0.5" stop-color="var(--parchment-light)"/>
          <stop offset="1" stop-color="var(--parchment-dark)"/>
        </linearGradient>
        <linearGradient id="foliage" x1="0" y1="0" x2="0" y2="1">
          <stop offset="0" stop-color="var(--sage)"/>
          <stop offset="1" stop-color="var(--sage)" stop-opacity="0"/>
        </linearGradient>
      </defs>
      <rect class="header-band" x="0" y="0" width="660" height="300" fill="var(--sage)"/>
      <rect class="foliage" x="0" y="300" width="660" height="270" fill="url(#foliage)"
            role="img" aria-label="Silhouettes of leaves and flowers trailing down from the header band"/>
      <path class="parchment-band" role="img" aria-label="Aged parchment texture with a torn top edge"
            d="M0 825 L60 815 L110 822 L170 808 L240 818 L300 805 L360 816 L420 806 L480 818 L540 804 L600 814 L660 808 L660 1075 L0 1075 Z"
            fill="url(#parchment)"/>
    </svg>

    <h1 class="business-name">Henri marsot<br>painting &amp; decorating</h1>

    <ul class="services">
      <li>Full service residential and<br>commercial painting</li>
      <li>Finest quality attention<br>to detail</li>
      <li>All workmanship guaranteed</li>
    </ul>

    <ul class="contact">
      <li>
        <svg class="icon" viewBox="0 0 22 22" aria-hidden="true">
          <rect x="3" y="3" width="16" height="16" rx="3" fill="none" stroke="var(--contact)" stroke-width="2"/>
        </svg>
        norabvantreel@mailbox-example.fr
      </li>
      <li>
        <svg class="icon" viewBox="0 0 22 22" aria-hidden="true">
          <circle cx="11" cy="11" r="4" fill="none" stroke="var(--contact)" stroke-width="2"/>
          <path d="M15 8 V13 A2.5 2.5 0 0 0 20 13 V11 A9 9 0 1 0 15 19" fill="none" stroke="var(--contact)" stroke-width="2"/>
        </svg>
        0417382650
      </li>
    </ul>
  </article>
</body>
</html>
```